self serve frozen yogurt store

would like a postcard to use for promotional purposes. We are a self serve frozen business in Alder Ridge Shopping Center located in Fairhaven, MD. We are opened 7 days a week. We offer 15 flavors and over 40 different toppings.

Store

```html
<!DOCTYPE html>
<html lang="en">
<head>
<meta charset="utf-8">
<title>Cherrywhip Frozen Yogurt – Promotional Postcard</title>
<link rel="stylesheet" href="https://fonts.googleapis.com/css2?family=Abril+Fatface&family=Archivo+Black&family=Mulish:wght@400;600;800&family=Playfair+Display:ital,wght@1,700&family=Poiret+One&display=swap">
<style>
  :root {
    --canvas: #edf1f1;
    --paper: #ffffff;
    --violet: #8a22ff;
    --violet-line: #9a4dff;
    --lavender: #e6e0f6;
    --wall: #7d63c9;
    --pink: #ff6fe0;
    --yellow: #fff27a;
    --lime: #d8f59a;
    --ink: #111111;
    --brand-red: #e8192c;
  }
  * { margin: 0; padding: 0; box-sizing: border-box; }
  html, body { width: 1200px; height: 1000px; overflow: hidden; }
  body { background: var(--canvas); font-family: "Mulish", Arial, sans-serif; position: relative; }

  .postcard { position: absolute; background: var(--paper); overflow: hidden; }
  .postcard--front { left: 125px; top: 178px; width: 412px; height: 319px; }
  .postcard--back  { left: 584px; top: 382px; width: 463px; height: 359px; }

  .store-photo {
    position: absolute; left: 0; top: 0; width: 412px; height: 288px;
    background: linear-gradient(160deg, #5f4ab3 0%, var(--wall) 45%, #a99ad9 100%);
  }
  .front-art { position: absolute; left: 0; top: 0; width: 412px; height: 288px; }
  .cup-photo {
    position: absolute; left: 0; top: 62px; width: 212px; height: 208px;
    border-radius: 40% 40% 46% 46%;
    background: radial-gradient(circle at 50% 38%, #fffbe8 0%, #f4e6d4 38%, #e05a52 62%, #f0a030 82%, rgba(240,160,48,0) 100%);
  }

  .hours-offer {
    position: absolute; left: 233px; top: 14px; width: 160px; color: var(--ink); line-height: 1;
  }
  .offer-row { display: flex; align-items: flex-end; gap: 3px; white-space: nowrap; }
  .offer-thin { font-family: "Poiret One", sans-serif; font-size: 19px; letter-spacing: -0.5px; }
  .offer-fig { font-family: "Abril Fatface", serif; font-size: 30px; }
  .offer-script { font-family: "Playfair Display", serif; font-style: italic; font-weight: 700; font-size: 12px; line-height: 1.05; }
  .offer-heavy { font-family: "Archivo Black", sans-serif; font-size: 15px; letter-spacing: 2px; margin: 3px 0 2px; }
  .offer-word { font-family: "Mulish", sans-serif; font-size: 15px; line-height: 0.95; }
  .offer-word b { font-weight: 800; }
  .offer-caps { font-family: "Mulish", sans-serif; font-weight: 600; font-size: 13px; letter-spacing: 1px; }
  .offer-big-thin { font-family: "Poiret One", sans-serif; font-size: 30px; }

  .brand { position: absolute; }
  .brand-name {
    display: flex; align-items: center; gap: 5px;
    font-family: "Mulish", sans-serif; font-weight: 800; color: var(--brand-red); line-height: 1; white-space: nowrap;
  }
  .brand-dot { display: inline-block; border-radius: 50%; background: var(--brand-red); }
  .brand-tag { font-family: "Mulish", sans-serif; font-weight: 600; color: var(--violet); letter-spacing: 0.5px; }
  .postcard--front .brand { left: 224px; top: 230px; }
  .postcard--front .brand-name { font-size: 26px; }
  .postcard--front .brand-dot { width: 16px; height: 16px; }
  .postcard--front .brand-tag { font-size: 11px; margin-top: 3px; padding-left: 4px; }

  .location-band {
    position: absolute; left: 0; bottom: 0; background: var(--violet); color: #fff;
    display: flex; align-items: center; justify-content: center; white-space: nowrap;
  }
  .postcard--front .location-band { width: 412px; height: 31px; font-size: 11px; }
  .postcard--back .location-band { width: 224px; height: 26px; font-size: 9px; }

  .back-decor { position: absolute; left: 0; top: 0; width: 463px; height: 359px; }
  .postcard--back .brand { left: 70px; top: 32px; }
  .postcard--back .brand-name { font-size: 23px; }
  .postcard--back .brand-dot { width: 14px; height: 14px; }
  .postcard--back .brand-tag { font-size: 9px; margin-top: 3px; padding-left: 4px; }

  .stamp-box { position: absolute; left: 348px; top: 25px; width: 86px; height: 90px; background: var(--violet); }
  .address-line { position: absolute; left: 250px; width: 184px; height: 1px; background: var(--violet-line); }
  .address-line--1 { top: 158px; }
  .address-line--2 { top: 192px; }
  .address-line--3 { top: 217px; }
  .address-line--4 { top: 251px; }
</style>
</head>
<body>

<section class="postcard postcard--front">
  <div class="store-photo" role="img" aria-label="Photo of the yogurt shop interior with purple walls, framed fruit prints and seating"></div>
  <svg class="front-art" viewBox="0 0 412 288" aria-hidden="true">
    <circle cx="300" cy="62" r="128" fill="var(--lavender)" opacity="0.92"/>
    <circle cx="177" cy="110" r="40" fill="var(--pink)" opacity="0.8"/>
    <circle cx="320" cy="179" r="13" fill="var(--lime)" opacity="0.85"/>
    <path d="M0 288 L0 250 Q240 250 412 160 L412 288 Z" fill="var(--paper)"/>
  </svg>
  <div class="cup-photo" role="img" aria-label="Photo of a cup of vanilla frozen yogurt topped with strawberries and blueberries, with bananas and oranges beside it"></div>

  <div class="hours-offer">
    <div class="offer-row"><span class="offer-thin">WE OPEN</span><span class="offer-fig">7</span><span class="offer-script">days<br>a week</span></div>
    <div class="offer-heavy">WE OFFER</div>
    <div class="offer-row"><span class="offer-fig">15</span><span class="offer-word"><b>Flavors</b><br>and over</span></div>
    <div class="offer-row"><span class="offer-big-thin">40</span><span class="offer-word"><b>different</b><br><span class="offer-caps">TOPPINGS</span></span></div>
  </div>

  <div class="brand">
    <div class="brand-name">Cherrywhip <span class="brand-dot"></span></div>
    <div class="brand-tag">FROZEN YOGURT</div>
  </div>

  <div class="location-band">Location: Alder Ridge Shopping Center in Fairhaven, MD</div>
</section>

<section class="postcard postcard--back">
  <svg class="back-decor" viewBox="0 0 463 359" aria-hidden="true">
    <circle cx="33" cy="38" r="38" fill="var(--pink)" opacity="0.8"/>
    <circle cx="88" cy="48" r="29" fill="var(--yellow)" opacity="0.85"/>
    <circle cx="50" cy="100" r="15" fill="var(--lime)"/>
  </svg>

  <div class="brand">
    <div class="brand-name">Cherrywhip <span class="brand-dot"></span></div>
    <div class="brand-tag">FROZEN YOGURT</div>
  </div>

  <div class="stamp-box"></div>
  <div class="address-line address-line--1"></div>
  <div class="address-line address-line--2"></div>
  <div class="address-line address-line--3"></div>
  <div class="address-line address-line--4"></div>

  <div class="location-band">Alder Ridge Shopping Center. Fairhaven, MD</div>
</section>

</body>
</html>
```